I need a business card for my Heating / Cooling Business. I've been in the business for 28 years. The name of the company is "Walt's Heating and Cooling".
Designers, I've attached an old business card we've used to copy the information.
Take off 15 years of experience
Business
Walt Pemberton and Marla Pemberton(740)-795-4758

```html
<!DOCTYPE html>
<html lang="en">
<head>
<meta charset="UTF-8">
<title>Walt's Heating and Cooling – Business Card</title>
<link rel="stylesheet" href="https://fonts.googleapis.com/css2?family=Arimo:wght@400&family=Tinos:ital,wght@1,700&display=swap">
<style>
  :root {
    --backdrop: #2b2d31;
    --card-navy: #262a6b;
    --band-white: #ffffff;
    --band-grey: #e4e4e6;
    --title-navy: #1f2466;
    --text-white: #ffffff;
  }
  * { margin: 0; padding: 0; box-sizing: border-box; }
  html, body {
    width: 1200px;
    height: 864px;
    overflow: hidden;
    background: var(--backdrop);
  }
  .stage {
    position: relative;
    width: 1200px;
    height: 864px;
  }
  .card {
    position: absolute;
    width: 600px;
    height: 340px;
    background: var(--card-navy);
    overflow: hidden;
    font-family: "Arimo", Arial, sans-serif;
    color: var(--text-white);
  }
  /* Back side: list of services */
  .card--back { left: 140px; top: 60px; }
  .services {
    position: absolute;
    left: 0; right: 0;
    top: 104px;
    text-align: center;
    font-size: 17px;
    line-height: 21px;
    letter-spacing: 0.2px;
  }
  /* Front side */
  .card--front { left: 460px; top: 464px; }
  .title-band {
    position: absolute;
    left: 0; top: 0;
    width: 100%;
    height: 150px;
    background: linear-gradient(180deg, var(--band-white) 0%, var(--band-white) 45%, var(--band-grey) 100%);
    display: flex;
    align-items: center;
    justify-content: center;
  }
  .company-name {
    font-family: "Tinos", "Times New Roman", serif;
    font-style: italic;
    font-weight: 700;
    font-size: 30px;
    color: var(--title-navy);
    letter-spacing: 0.3px;
  }
  .owner {
    position: absolute;
    right: 338px;
    top: 186px;
    text-align: right;
    font-size: 17px;
    line-height: 20px;
  }
  .contact {
    position: absolute;
    left: 280px;
    top: 186px;
    font-size: 17px;
    line-height: 20px;
  }
  .contact-row {
    display: flex;
    align-items: flex-start;
    gap: 10px;
    margin-bottom: 2px;
  }
  .contact-icon {
    flex: 0 0 16px;
    width: 16px;
    height: 16px;
    margin-top: 2px;
  }
</style>
</head>
<body>
<main class="stage">

  <section class="card card--back" aria-label="Business card, back">
    <p class="services">
      Installation and Service Small Appliance Repair<br>
      Plumbing Refrigeration and Car Air Conditioning<br>
      Professional Mobile Home Installation
    </p>
  </section>

  <section class="card card--front" aria-label="Business card, front">
    <header class="title-band">
      <h1 class="company-name">Walt's Heating and Cooling</h1>
    </header>

    <div class="owner">
      <p>Walt Pemberton</p>
      <p>Marla Pemberton</p>
      <p>Certified Repairman</p>
    </div>

    <div class="contact">
      <div class="contact-row">
        <svg class="contact-icon" viewBox="0 0 16 16" aria-hidden="true">
          <rect width="16" height="16" rx="2" fill="#ffffff"/>
          <path d="M3.5 6.5 C3.5 4.5 12.5 4.5 12.5 6.5 L12.5 7.5 L10.5 7.5 L10.5 6.5 L5.5 6.5 L5.5 7.5 L3.5 7.5 Z" fill="#262a6b"/>
          <rect x="4.5" y="8.5" width="7" height="4" rx="0.8" fill="#262a6b"/>
        </svg>
        <span>(555) 312-9064</span>
      </div>
      <div class="contact-row">
        <svg class="contact-icon" viewBox="0 0 16 16" aria-hidden="true">
          <rect width="16" height="16" rx="2" fill="#ffffff"/>
          <path d="M8 2.8 C5.7 2.8 4.2 4.4 4.2 6.4 C4.2 9 8 13.2 8 13.2 C8 13.2 11.8 9 11.8 6.4 C11.8 4.4 10.3 2.8 8 2.8 Z" fill="#262a6b"/>
          <circle cx="8" cy="6.4" r="1.5" fill="#ffffff"/>
        </svg>
        <span>48210 Birch Hollow Drive<br>Millbrook Point, Ohio 43900</span>
      </div>
    </div>
  </section>

</main>
</body>
</html>
```